Tech business card design

We need an amazing business card design for our new business 'Brakka' a marketing tech startup based in Sydney, Australia. We provide an online marketplace for businesses to search and buy advertising media, connect with service providers and learn more about marketing. We wish to communicate 'cool tech', reliability and professionalism and design based around our logo.

Target Market(s)

Business Owners

Contact Information for Business Card

Name
Position
Email Address
Website
Phone Number

Font styles to use
Other font styles liked:
• Avenir & Avenir Next

Colors

Designer to choose colors to be used in the design.

```html
<!DOCTYPE html>
<html lang="en">
<head>
<meta charset="utf-8">
<title>Brakka Business Card</title>
<link href="https://fonts.googleapis.com/css2?family=Nunito+Sans:wght@400;600;800&display=swap" rel="stylesheet">
<style>
  :root {
    --navy: #14164a;
    --white: #ffffff;
    --stage: #2b2b2d;
    --grey-text: #55575f;
    --band-text: #e9eaf5;
  }
  * { margin: 0; padding: 0; box-sizing: border-box; }
  html, body {
    width: 1200px; height: 892px; overflow: hidden;
    background: var(--stage);
    font-family: "Nunito Sans", "Avenir Next", Avenir, sans-serif;
  }
  .stage {
    width: 1200px; height: 892px;
    display: flex; align-items: center; justify-content: center; gap: 40px;
  }
  .card {
    position: relative;
    width: 540px; height: 309px;
    background: var(--white);
    box-shadow: 0 10px 30px rgba(0,0,0,0.45);
    overflow: hidden;
  }
  .wordmark {
    color: var(--navy);
    font-weight: 800;
    letter-spacing: -0.02em;
    line-height: 1;
  }
  /* back side */
  .card-back .brand-block {
    position: absolute; right: 40px; bottom: 62px;
    text-align: right;
  }
  .card-back .wordmark { font-size: 46px; }
  .card-back .site {
    margin-top: 4px;
    font-size: 15px; color: var(--grey-text); letter-spacing: 0.02em;
  }
  /* front side */
  .card-front .wordmark {
    position: absolute; left: 0; right: 0; top: 66px;
    text-align: center; font-size: 74px;
  }
  .info-band {
    position: absolute; left: 0; right: 0; top: 168px; height: 84px;
    background: var(--navy);
    display: flex; align-items: center; justify-content: center;
    color: var(--band-text);
  }
  .person { text-align: right; padding-right: 20px; }
  .person-name {
    font-weight: 800; font-size: 21px; text-transform: uppercase;
    color: var(--white); letter-spacing: 0.01em;
  }
  .person-role { font-size: 15px; text-transform: uppercase; letter-spacing: 0.02em; }
  .divider { width: 1px; height: 58px; background: var(--band-text); opacity: 0.8; }
  .contacts { list-style: none; padding-left: 20px; font-size: 13.5px; line-height: 1.45; }
  .contacts li { display: flex; align-items: center; gap: 8px; }
  .contacts svg { width: 12px; height: 12px; flex: none; }
</style>
</head>
<body>
<main class="stage">
  <section class="card card-back">
    <div class="brand-block">
      <div class="wordmark">brakka</div>
      <div class="site">brakkamedia.com.au</div>
    </div>
  </section>

  <section class="card card-front">
    <div class="wordmark">brakka</div>
    <div class="info-band">
      <div class="person">
        <div class="person-name">Liam Foster</div>
        <div class="person-role">Founder, Director</div>
      </div>
      <div class="divider"></div>
      <ul class="contacts">
        <li>
          <svg viewBox="0 0 12 12" aria-hidden="true"><rect x="3" y="0.5" width="6" height="11" rx="1" fill="none" stroke="currentColor" stroke-width="1.2"/><circle cx="6" cy="9.6" r="0.7" fill="currentColor"/></svg>
          +61 (0)400 555 218
        </li>
        <li>
          <svg viewBox="0 0 12 12" aria-hidden="true"><rect x="0.5" y="2.5" width="11" height="7.5" fill="currentColor"/><path d="M0.8 2.8 L6 7 L11.2 2.8" fill="none" stroke="#14164a" stroke-width="1"/></svg>
          liam@brakkamedia.com.au
        </li>
        <li>
          <svg viewBox="0 0 12 12" aria-hidden="true"><circle cx="6" cy="6" r="5.5" fill="currentColor"/><path d="M0.5 6 H11.5 M6 0.5 C3 3.5 3 8.5 6 11.5 M6 0.5 C9 3.5 9 8.5 6 11.5" fill="none" stroke="#14164a" stroke-width="0.8"/></svg>
          www.brakkamedia.com.au
        </li>
      </ul>
    </div>
  </section>
</main>
</body>
</html>
```